Label Sticker Design for Apothecary Brand

Hello! We are an independent grassroots business located in Ontario, Canada that specializes in making organic botanical and herbal skin care, tea, witchcraft and wellness products. We have been in business for 5 years and are looking to create a label sticker with one of our slogans for use in packaging.

Our brand is dark, herbal, witchy, and modern with old-world apothecary and vintage influences. We want a label that will be VERY clean, and easily explain what our product is, while conveying a sense of mysticism and magic, as well as a traditional apothecary vibe.

We have attached design inspiration to give you an idea of the style that we would like. Our demographic is hipster, current, (think finger tattoos, linen dresses, and organic groceries), and they care deeply about where we source our ingredients, and how we craft our product. We don't want an old-school sticker that looks like it should be on the shelves of a health food store. The design should be contemporary, upmarket, modern and clean, but evoke a strong sense of magic and self-care with wild gathered herbs and unusual wild flowers!

This will be used as a packaging sticker for our shipping boxes.

We look forward to your winning design!
Thank you very much.

Target Market(s)

20 - 50yr Female Demographic
Natural, bohemian, earthy, hipster and modern

Key Words: Minimalist Tattoos, Organic Skin Care, Bohemian, Witchy, Dark, Moody, Confident, Sustainable, Ethical,

PLEASE VIEW PHOTOS BEFORE SUBMITTING A DESIGN ;)

Industry/Entity Type

Skin Care Product

Font styles to use
Serif
Script

Colors
1b1b1b
5c5c5c
fbfbfb

Requirements
Must have
• Clean and Simple - Take a look at the photos we've posted!
• Black / greyscale (No color)
• Label sticker must be a rectangle (3" x 2")
• Very Modern with a touch of old-world
• We are open to a variety of font styles. Please see photo FONT in image files, or the images 'Bottle Inspiration'
• Please use the following text:
• Thornmoor Stillhouse
• --------------------
• Crafted with Magic
• * Once your design is chosen and purchased, we will require the names of all fonts and sources of imagery used.
Nice to have
• A moody botanical graphic surrounding the text. Tangled wild, antique botanical illustrations. Not mandatory, but would be very nice.
Should not have
• Colour
• Messy or overly dramatic fonts
• Cartoon Imagery
• Leaf Motif
• Female Body Silhouettes
• Scroll or decorative borders.
• Butterflies, birds etc
• Actual pictures of witches
• Mandalas or Messy Graphics

```html
<!DOCTYPE html>
<html lang="en">
<head>
<meta charset="UTF-8">
<title>Thornmoor Stillhouse — Crafted with Magic Label</title>
<link rel="stylesheet" href="https://fonts.googleapis.com/css2?family=Courier+Prime:wght@400;700&display=swap">
<style>
  :root {
    --ink: #1b1b1b;
    --ink-soft: #5c5c5c;
    --paper: #fbfbfb;
    --backdrop: #f1efec;
    --silver-edge: #d6d6d6;
    --silver-mid: #e4e4e4;
    --silver-light: #f7f7f7;
    --art-light: #ececec;
    --art-dark: #cfcfcf;
  }
  * { margin: 0; padding: 0; box-sizing: border-box; }
  html, body {
    width: 1091px;
    height: 1200px;
    overflow: hidden;
    background: var(--backdrop);
  }
  .canvas {
    position: relative;
    width: 1091px;
    height: 1200px;
  }
  .label {
    position: absolute;
    left: 153px;
    top: 100px;
    width: 784px;
    height: 1000px;
    background: linear-gradient(90deg,
      var(--silver-edge) 0%,
      var(--silver-mid) 18%,
      var(--silver-light) 42%,
      var(--paper) 52%,
      var(--silver-light) 62%,
      var(--silver-mid) 84%,
      var(--silver-edge) 100%);
    color: var(--ink);
    text-align: center;
  }
  .brand-name {
    position: absolute;
    top: 98px;
    left: 0;
    width: 100%;
    font-family: "Courier Prime", monospace;
    font-weight: 700;
    font-size: 80px;
    line-height: 90px;
    letter-spacing: 0;
    color: var(--ink);
  }
  .botanical-art {
    position: absolute;
    left: 211px;
    top: 306px;
    width: 342px;
    height: 378px;
    border-radius: 46%;
    background: radial-gradient(ellipse at center, var(--art-dark) 0%, var(--art-light) 65%, transparent 100%);
  }
  .slogan {
    position: absolute;
    top: 736px;
    left: 0;
    width: 100%;
    font-family: "Courier Prime", monospace;
    font-weight: 400;
    font-size: 66px;
    line-height: 64px;
    color: var(--ink);
  }
  .volume {
    position: absolute;
    top: 905px;
    left: 0;
    width: 100%;
    font-family: "Courier Prime", monospace;
    font-weight: 400;
    font-size: 60px;
    line-height: 70px;
    letter-spacing: 2px;
    color: var(--ink);
  }
</style>
</head>
<body>
  <main class="canvas">
    <section class="label">
      <h1 class="brand-name">Thornmoor<br>Stillhouse</h1>
      <div class="botanical-art" role="img" aria-label="Black ink line drawing of a sprig of wild mint leaves"></div>
      <p class="slogan">Crafted<br>with Magic</p>
      <p class="volume">50 Ml</p>
    </section>
  </main>
</body>
</html>
```